Frozen Yoghurt
Aufgabenstellung
Es soll eine Postkarte erstellt werden
auf die Vorteile des Produkts dargestellt werden
- kein fett (98% fettfrei)
- keine künstlichen süssungsmittel
- low calorien
- Viel Calcium
- Viel Eiweiss
- Vitamine durch Frucht topping
Die Postkarte soll gleichzeitig dazu dienen dass man sie mit zu uns ins Geschäft bringt und dann ein gratis Muster bekommt.
Mitbewerber: www.plumdrizzle.com, www.velvocup.com

```html
<!DOCTYPE html>
<html lang="de">
<head>
<meta charset="utf-8">
<title>Frozen Yoghurt – Postkarte</title>
<link href="https://fonts.googleapis.com/css2?family=Open+Sans:wght@400;600;700&display=swap" rel="stylesheet">
<style>
  :root {
    --green: #2f8a12;
    --green-light: #8cc63e;
    --magenta: #e0187f;
    --orange: #ee7d1c;
    --white: #ffffff;
    --page: #ffffff;
    --frame: #9a9a9a;
    --photo-warm: #b98a6e;
    --photo-deep: #5d3a2c;
    --cup-cream: #f1ede6;
    --berry: #3a4a78;
  }
  * { margin: 0; padding: 0; box-sizing: border-box; }
  html, body { width: 1200px; height: 848px; overflow: hidden; background: var(--page); }
  body { position: relative; font-family: "Open Sans", Arial, sans-serif; }

  .card {
    position: absolute; top: 123px; width: 419px; height: 593px;
    background: var(--white); border: 1px solid var(--frame); overflow: hidden;
  }
  .card--front { left: 123px; }
  .card--back { left: 651px; }

  .wave { position: absolute; left: 0; width: 100%; display: block; }

  .brand {
    position: absolute; display: flex; align-items: center; gap: 5px;
    font-size: 11px; font-weight: 600; color: var(--white); white-space: nowrap;
  }
  .brand__dot { width: 10px; height: 10px; border-radius: 50%; background: var(--magenta); }

  /* front */
  .front__brand { left: 16px; top: 12px; }
  .headline-old {
    position: absolute; left: 24px; top: 78px; font-size: 33px; color: var(--orange);
  }
  .headline-old s { text-decoration-thickness: 2px; }
  .headline-old span { color: var(--magenta); }
  .headline-main {
    position: absolute; left: 106px; top: 100px; font-size: 64px; color: var(--magenta);
    transform: rotate(-6deg); transform-origin: left bottom; letter-spacing: 1px;
  }
  .front__product {
    position: absolute; left: 40px; top: 180px; width: 330px; height: 250px;
    background: radial-gradient(closest-side, var(--cup-cream) 0 55%, #d9c4a0 75%, var(--berry) 92%, transparent 100%);
  }
  .front__claim {
    position: absolute; left: 12px; top: 432px; font-size: 27px; font-weight: 700;
    color: var(--green); transform: rotate(-6deg); transform-origin: left bottom; white-space: nowrap;
  }

  /* back */
  .back__photo {
    position: absolute; left: 0; top: 0; width: 253px; height: 190px;
    background: linear-gradient(135deg, var(--photo-deep), var(--photo-warm) 55%, #e3c7b2);
  }
  .offer {
    position: absolute; left: 253px; top: 0; width: 166px; height: 190px;
    background: var(--green-light); border-left: 2px dashed var(--white);
    text-align: right; padding: 8px 8px 0 0; color: var(--white);
  }
  .offer__title { font-size: 38px; color: var(--magenta); line-height: 1.1; white-space: nowrap; }
  .offer__text { font-size: 14.5px; line-height: 1.5; margin-top: 8px; }
  .offer__text em { font-style: normal; color: var(--orange); }
  .back__title {
    position: absolute; left: 20px; top: 210px; font-size: 38px; font-weight: 400; color: var(--green-light);
    transform: rotate(-3deg); transform-origin: left bottom; white-space: nowrap;
  }
  .benefits { position: absolute; left: 16px; top: 270px; font-size: 15.5px; line-height: 1.55; color: var(--orange); }
  .benefits__lead { color: var(--magenta); font-weight: 700; }
  .benefits ul { list-style: none; }
  .benefits li { padding-left: 14px; text-indent: -14px; }
  .benefits li::before { content: "• "; }
  .benefits li.benefits__cont { text-indent: 0; }
  .benefits li.benefits__cont::before { content: none; }
  .back__product { position: absolute; }
  .back__product--large { left: 276px; top: 335px; width: 134px; height: 115px;
    background: radial-gradient(closest-side, var(--cup-cream) 0 55%, #d5b88e 75%, var(--berry) 92%, transparent 100%); }
  .back__product--a { left: 22px; top: 440px; width: 62px; height: 70px;
    background: radial-gradient(closest-side, #e9d2b4 0 60%, #c9522e 88%, transparent 100%); }
  .back__product--b { left: 98px; top: 420px; width: 70px; height: 88px;
    background: radial-gradient(closest-side, #f4e6c8 0 60%, #d7a253 88%, transparent 100%); }
  .back__product--c { left: 178px; top: 420px; width: 66px; height: 78px;
    background: radial-gradient(closest-side, var(--cup-cream) 0 58%, var(--berry) 88%, transparent 100%); }
  .address {
    position: absolute; right: 180px; top: 515px; text-align: right; font-style: normal;
    font-size: 15px; line-height: 1.45; color: var(--white);
  }
  .back__brand { right: 24px; top: 548px; }
</style>
</head>
<body>

<section class="card card--front">
  <svg class="wave" style="top:0" width="419" height="70" viewBox="0 0 419 70" preserveAspectRatio="none">
    <path d="M0 0H419V38C300 30 200 62 0 58Z" fill="var(--green)"/>
    <path d="M0 58C200 62 300 30 419 38V44C300 38 200 68 0 64Z" fill="var(--green-light)"/>
  </svg>
  <div class="brand front__brand"><span class="brand__dot"></span>Fresh Pantry</div>

  <div class="front__product" role="img" aria-label="Becher Frozen Yoghurt mit Müsli und Beeren"></div>

  <div class="headline-old"><s>Sünd</s><span>e?</span></div>
  <div class="headline-main">Genuss!</div>

  <div class="front__claim">Ohne schlechtes Gewissen!</div>

  <svg class="wave" style="bottom:0" width="419" height="120" viewBox="0 0 419 120" preserveAspectRatio="none">
    <path d="M0 28C140 40 260 74 419 40V120H0Z" fill="var(--magenta)"/>
    <path d="M0 48C150 58 270 96 419 70V120H0Z" fill="var(--white)"/>
    <path d="M0 82C150 80 280 110 419 92V100C280 118 150 90 0 92Z" fill="var(--orange)"/>
    <path d="M0 96C150 94 280 120 419 106V120H0Z" fill="var(--magenta)"/>
  </svg>
</section>

<section class="card card--back">
  <div class="back__photo" role="img" aria-label="Foto: drei Freundinnen geniessen Frozen Yoghurt"></div>
  <div class="offer">
    <div class="offer__title">Taste it!</div>
    <p class="offer__text">Karte mitbringen und einen Frozen Yoghurt nach Deiner Wahl <em>kostenlos</em> testen!</p>
  </div>

  <svg class="wave" style="top:150px" width="419" height="80" viewBox="0 0 419 80" preserveAspectRatio="none">
    <path d="M0 40C140 20 280 30 419 8V22C280 44 140 34 0 56Z" fill="var(--magenta)"/>
    <path d="M0 56C140 34 280 44 419 22V30C280 52 140 58 0 78Z" fill="var(--white)"/>
    <path d="M0 70C150 50 280 58 419 40V48C280 64 150 62 0 80Z" fill="var(--orange)"/>
  </svg>

  <h1 class="back__title">Frozen Yoghurt</h1>

  <div class="benefits">
    <p class="benefits__lead">Genieße ohne schlechtes Gewissen!</p>
    <p>Unser Frozen Yoghurt ist</p>
    <ul>
      <li>100 % kalorienarm und</li>
      <li>ohne künstliche Süßungsmittel</li>
      <li class="benefits__cont">plus mehr</li>
      <li>Calcium, Eiweiß &amp; Vitamine</li>
    </ul>
  </div>

  <div class="back__product back__product--large" role="img" aria-label="Becher Frozen Yoghurt mit Beeren"></div>
  <div class="back__product back__product--a" role="img" aria-label="Frozen Yoghurt mit Himbeersauce"></div>
  <div class="back__product back__product--b" role="img" aria-label="Frozen Yoghurt mit Karamell"></div>
  <div class="back__product back__product--c" role="img" aria-label="Frozen Yoghurt mit Brombeeren"></div>

  <svg class="wave" style="bottom:0" width="419" height="110" viewBox="0 0 419 110" preserveAspectRatio="none">
    <path d="M0 40C150 20 300 0 419 6V14C300 10 150 30 0 50Z" fill="var(--green-light)"/>
    <path d="M0 50C150 30 300 12 419 14V110H0Z" fill="var(--green)"/>
  </svg>
  <address class="address">Im Marktforum<br>Lindengasse 12-14<br>3000 Bern</address>
  <div class="brand back__brand"><span class="brand__dot"></span>Fresh Pantry</div>
</section>

</body>
</html>
```